Step and Repeat Backdrop for wedding reception photo booth

Would like to have a Step and Repeat Backdrop (8 foot high by 10 foot wide) that incorporates the wedding logo (attached) and the names Clara and Bruno. Background should be white, and wedding colors are burgundy and gold. Show me creativity :-) I have included some random samples.

```html
<!DOCTYPE html>
<html lang="en">
<head>
<meta charset="utf-8">
<title>Clara &amp; Bruno — Step and Repeat Backdrop</title>
<link rel="stylesheet" href="https://fonts.googleapis.com/css2?family=Great+Vibes&family=Playfair+Display:wght@500&display=swap">
<style>
  :root {
    --paper: #ffffff;
    --burgundy: #9b0a10;
    --gold: #b08a4a;
    --gold-light: #d8bd7f;
    --gold-pale: #efe2c4;
    --blush: #e6c3c5;
    --frame-line: #e8dcc0;
  }
  html, body {
    margin: 0;
    padding: 0;
    width: 1200px;
    height: 900px;
    overflow: hidden;
    background: var(--paper);
  }
  .backdrop {
    display: block;
    width: 1200px;
    height: 900px;
  }
  .repeat-mark {
    font-family: "Playfair Display", serif;
    font-weight: 500;
    font-size: 40px;
    fill: var(--blush);
  }
  .couple-names {
    font-family: "Great Vibes", cursive;
    font-size: 150px;
    fill: var(--burgundy);
  }
  .center-mark {
    font-family: "Playfair Display", serif;
    font-weight: 500;
    font-size: 140px;
    fill: var(--gold);
  }
  .frame-line {
    fill: none;
    stroke: var(--frame-line);
    stroke-width: 1;
  }
</style>
</head>
<body>
<svg class="backdrop" viewBox="0 0 1200 900" xmlns="http://www.w3.org/2000/svg">
  <defs>
    <linearGradient id="ornament-gold-h" x1="0" y1="0" x2="1" y2="0">
      <stop offset="0" stop-color="var(--gold-pale)"/>
      <stop offset="0.5" stop-color="var(--gold-light)" stop-opacity="0.55"/>
      <stop offset="1" stop-color="var(--gold-pale)"/>
    </linearGradient>
    <linearGradient id="ornament-gold-v" x1="0" y1="0" x2="0" y2="1">
      <stop offset="0" stop-color="var(--gold-pale)"/>
      <stop offset="0.5" stop-color="var(--gold-light)" stop-opacity="0.55"/>
      <stop offset="1" stop-color="var(--gold-pale)"/>
    </linearGradient>
    <path id="names-arc" d="M 235 390 Q 605 40 975 380"/>
  </defs>

  <rect class="frame-line" x="126.5" y="71.5" width="953" height="762"/>

  <g class="ornament-border">
    <rect x="158" y="84" width="892" height="46" rx="6" fill="url(#ornament-gold-h)" role="img" aria-label="Gold filigree scroll border along the top edge"/>
    <rect x="158" y="774" width="892" height="46" rx="6" fill="url(#ornament-gold-h)" role="img" aria-label="Gold filigree scroll border along the bottom edge"/>
    <rect x="141" y="112" width="44" height="684" rx="6" fill="url(#ornament-gold-v)" role="img" aria-label="Gold filigree scroll border along the left edge"/>
    <rect x="1021" y="112" width="44" height="684" rx="6" fill="url(#ornament-gold-v)" role="img" aria-label="Gold filigree scroll border along the right edge"/>
  </g>

  <g class="repeat-pattern" text-anchor="middle">
    <text class="repeat-mark" x="240" y="188">C&amp;B</text>
    <text class="repeat-mark" x="362" y="188">C&amp;B</text>
    <text class="repeat-mark" x="483" y="188">C&amp;B</text>
    <text class="repeat-mark" x="603" y="188">C&amp;B</text>
    <text class="repeat-mark" x="725" y="188">C&amp;B</text>
    <text class="repeat-mark" x="845" y="188">C&amp;B</text>
    <text class="repeat-mark" x="965" y="188">C&amp;B</text>

    <text class="repeat-mark" x="240" y="281">C&amp;B</text>
    <text class="repeat-mark" x="362" y="281">C&amp;B</text>
    <text class="repeat-mark" x="725" y="281">C&amp;B</text>
    <text class="repeat-mark" x="845" y="281">C&amp;B</text>
    <text class="repeat-mark" x="965" y="281">C&amp;B</text>

    <text class="repeat-mark" x="240" y="376">C&amp;B</text>
    <text class="repeat-mark" x="362" y="376">C&amp;B</text>
    <text class="repeat-mark" x="845" y="376">C&amp;B</text>
    <text class="repeat-mark" x="965" y="376">C&amp;B</text>

    <text class="repeat-mark" x="240" y="466">C&amp;B</text>
    <text class="repeat-mark" x="362" y="466">C&amp;B</text>
    <text class="repeat-mark" x="845" y="466">C&amp;B</text>
    <text class="repeat-mark" x="965" y="466">C&amp;B</text>

    <text class="repeat-mark" x="240" y="559">C&amp;B</text>
    <text class="repeat-mark" x="362" y="559">C&amp;B</text>
    <text class="repeat-mark" x="845" y="559">C&amp;B</text>
    <text class="repeat-mark" x="965" y="559">C&amp;B</text>

    <text class="repeat-mark" x="240" y="654">C&amp;B</text>
    <text class="repeat-mark" x="362" y="654">C&amp;B</text>
    <text class="repeat-mark" x="483" y="654">C&amp;B</text>
    <text class="repeat-mark" x="603" y="654">C&amp;B</text>
    <text class="repeat-mark" x="725" y="654">C&amp;B</text>
    <text class="repeat-mark" x="845" y="654">C&amp;B</text>
    <text class="repeat-mark" x="965" y="654">C&amp;B</text>

    <text class="repeat-mark" x="240" y="747">C&amp;B</text>
    <text class="repeat-mark" x="362" y="747">C&amp;B</text>
    <text class="repeat-mark" x="483" y="747">C&amp;B</text>
    <text class="repeat-mark" x="603" y="747">C&amp;B</text>
    <text class="repeat-mark" x="725" y="747">C&amp;B</text>
    <text class="repeat-mark" x="845" y="747">C&amp;B</text>
    <text class="repeat-mark" x="965" y="747">C&amp;B</text>
  </g>

  <text class="couple-names" text-anchor="middle">
    <textPath href="#names-arc" startOffset="50%">Clara &amp; Bruno</textPath>
  </text>

  <text class="center-mark" x="605" y="500" text-anchor="middle">C&amp;B</text>
</svg>
</body>
</html>
```